Design a label for a range of honey under :BRIGHT MEADOW HONEY. (Original quirky different)

Create a label for a range of honey products under the brand BRIGHT MEADOW HONEY.
Iam the beekeeper and want to sell for the local New Zealand market directly to the consumer, online mainly.
Brand position: A contemporary honey, a fresh look for a simple product, like nature intended, nothing taken out, nothing added. Doesnt take itself seriously.
Personality: Contemporary, fresh, modern, free and fun,loving. Doesnt take itself seriously, loving, generous, upbeat, provide enjoyment, life ...
Brand value: Straight up, keep it simple, generous, different,
Label: Modern twist of nature and goodness (no straight picture of nature) quirky?, use of slogan? ( Nature in a pot / More than just honey / Taste of nature / It's all good...
Need to stand out, make you smile, be noticed, different...

Target Market(s)

Online direct customer.

Requirements
Must have
• legal requirements for NZ labeling attached.
A twist and quirky side...
Should not have
• Basic picture of nature.
Straight forward boring everybody else's feel.

```html
<!DOCTYPE html>
<html lang="en">
<head>
<meta charset="utf-8">
<title>Bright Meadow Honey – Label</title>
<link rel="stylesheet" href="https://fonts.googleapis.com/css2?family=Arimo:wght@400;700&display=swap">
<style>
  :root {
    --backdrop: #575152;
    --label-white: #ffffff;
    --honey-pale: #fff6b8;
    --honey-light: #fffbd6;
    --honey-mid: #fff09a;
    --ink: #161a19;
  }
  html, body {
    margin: 0;
    padding: 0;
    width: 1200px;
    height: 1200px;
    overflow: hidden;
    background: var(--backdrop);
  }
  .canvas {
    position: relative;
    width: 1200px;
    height: 1200px;
    background: var(--backdrop);
    font-family: "Arimo", Arial, sans-serif;
    color: var(--ink);
  }
  .label {
    position: absolute;
    left: 150px;
    top: 150px;
    width: 900px;
    height: 900px;
    background: var(--label-white);
  }
  .label__field {
    position: absolute;
    left: 27px;
    right: 27px;
    top: 29px;
    height: 840px;
    background: radial-gradient(circle at 50% 45%, var(--honey-light) 0%, var(--honey-pale) 70%, var(--honey-mid) 100%);
  }
  .label__emblem {
    position: absolute;
    left: 50%;
    top: 40px;
    width: 210px;
    height: 210px;
    margin-left: -105px;
    border-radius: 50%;
    background: var(--honey-mid);
  }
  .label__text {
    position: absolute;
    left: 0;
    right: 0;
    margin: 0;
    text-align: center;
    white-space: nowrap;
  }
  .brand-name {
    top: 312px;
    font-size: 60px;
    font-weight: 700;
    letter-spacing: 4px;
  }
  .product-name {
    top: 393px;
    font-size: 192px;
    font-weight: 400;
    line-height: 1;
    letter-spacing: 2px;
  }
  .tagline {
    top: 610px;
    font-size: 40px;
    letter-spacing: 5px;
  }
  .producer {
    top: 727px;
    font-size: 31px;
    line-height: 38px;
    letter-spacing: 4px;
  }
  .net-weight {
    position: absolute;
    left: 50%;
    bottom: 0;
    width: 86px;
    height: 60px;
    margin-left: -43px;
    background: var(--ink);
    color: var(--label-white);
    font-size: 25px;
    line-height: 60px;
    text-align: center;
    letter-spacing: 1px;
  }
  .batch-code {
    position: absolute;
    left: 26px;
    bottom: 7px;
    font-size: 14px;
    font-weight: 700;
    letter-spacing: 1px;
  }
</style>
</head>
<body>
<main class="canvas">
  <section class="label">
    <div class="label__field" role="img" aria-label="Soft pale yellow honeycomb pattern background"></div>
    <div class="label__emblem"></div>
    <p class="label__text brand-name">BRIGHT MEADOW</p>
    <h1 class="label__text product-name">HONEY</h1>
    <p class="label__text tagline">MORE THAN JUST HONEY</p>
    <p class="label__text producer">HILLCREST PANTRY LTD<br>48 KOWHAI RD WELLINGTON, NZ</p>
    <div class="net-weight">500g</div>
    <div class="batch-code">274 ABC</div>
  </section>
</main>
</body>
</html>
```